Psychology Practice in Sydney Website Redesign

Corvale Psychology is a Psychology Practice with locations in Westmead, Chatswood and the CBD. They have specialties in treating children, and in treating eating disorders. They also treat anxiety and depression. They have ~10-20 clinical psychologists working for them.

The client wants the site to be modern and professional, he said:
”Mainly gonna be the credibility, people already know of us, but some could find us on finderly search, site needs to be a bit sexy.”

The client prefers websites with a heavy use of negative space and a largely minimal, modern design. (e.g. https://harbourlanemind.example.au/, https://www.kinloft.example.au/, https://tallowpath.example.au/). He wants the site to be approachable without being unprofessional, and to be modern without being clinical. This is their current site: https://www.corvalepsychology.example.au/

The client wants the site to be a one pager design (like the sites given above). Please include a section named “Our Specialisations”, and the next titled “What we treat”, then one titled “Our Team” Feel free to take inspiration from the included links for the layout of these parts of the site.

Please mock up a booking panel similar to the that appears when you click "book now" on https://www.mindquaytalk.example.au/# .

The client would prefer you use the current logo and colour green (in logo) for theming.

Current site: https://www.corvalepsychology.example.au/

The winning designers will be required to:
- Provide a secondary standard page template
- Provide a design for a flyout enquiry/booking form
- Supply all images used in the designs free of charge

```html
<!DOCTYPE html>
<html lang="en">
<head>
<meta charset="utf-8">
<title>Corvale &amp; Associates – Clinical Psychologists</title>
<link href="https://fonts.googleapis.com/css2?family=Figtree:wght@400;500;600;700&display=swap" rel="stylesheet">
<style>
:root{
  --green:#74c48b;
  --green-soft:#effcf2;
  --ink:#151515;
  --muted:#555;
  --black:#000;
  --footer:#f2f2f2;
  --white:#fff;
}
*{box-sizing:border-box;margin:0;padding:0}
html,body{width:1200px;height:5287px;overflow:hidden}
body{position:relative;background:var(--white);font-family:"Figtree",Helvetica,Arial,sans-serif;color:var(--ink)}
.abs{position:absolute}
.topbar{top:0;left:0;width:1200px;height:86px}
.brand{display:flex;align-items:center;gap:10px;color:var(--green);font-weight:700;font-size:22px;letter-spacing:.5px;text-transform:uppercase}
.brand-square{width:16px;height:16px;background:var(--green)}
.topbar .brand{position:absolute;left:164px;top:28px}
.enquiries{position:absolute;right:164px;top:33px;font-size:17px;font-weight:600}
.enquiries span{color:var(--green);margin-left:14px}
.mainnav{top:86px;left:0;width:1200px;height:72px;background:var(--black);display:flex;align-items:center;padding-left:162px}
.mainnav a{color:var(--white);text-decoration:none;font-size:14px;font-weight:600;margin-right:31px}
.mainnav a.active{color:var(--green)}
.btn-book{position:absolute;left:900px;top:19px;width:136px;height:35px;background:var(--green);color:var(--white);font-size:13px;font-weight:600;display:flex;align-items:center;justify-content:center;border-radius:3px;letter-spacing:.5px}
.hero-title{left:160px;top:312px;width:500px;text-align:center;color:var(--green);font-size:52px;font-weight:500;line-height:56px;letter-spacing:-1px}
.hero-text{left:196px;top:441px;width:428px;text-align:center;font-size:15px;line-height:22px;letter-spacing:.3px}
.photo{position:absolute}
.photo .fill{position:absolute;inset:0 0 12px 0}
.photo .bar{position:absolute;left:0;right:0;bottom:0;height:12px;background:var(--green)}
.section-title{left:0;width:1200px;text-align:center;color:var(--green);font-size:25px;font-weight:600;letter-spacing:-.3px}
.band{left:0;width:1200px;background:var(--green-soft)}
.spec-item{top:826px;width:200px;text-align:center;font-size:20px;font-weight:500;line-height:23px;color:var(--black)}
.divider{top:830px;width:2px;height:40px;background:var(--ink)}
.btn-outline{width:121px;height:28px;border:1.5px solid var(--ink);border-radius:14px;font-size:15px;display:flex;align-items:center;justify-content:center}
.treat h3{font-size:26px;font-weight:600;letter-spacing:-.5px;margin-bottom:14px}
.treat p{font-size:15px;line-height:22px;letter-spacing:.2px;width:305px}
.treat.narrow p{width:260px}
.member{width:330px;text-align:center}
.member .avatar{width:124px;height:124px;margin:0 auto;position:relative}
.member .avatar .bar{position:absolute;left:0;right:0;bottom:0;height:5px;background:var(--green)}
.member h4{margin-top:38px;font-size:22px;font-weight:600;letter-spacing:-.4px}
.member p{margin-top:10px;font-size:13px;line-height:18px;color:var(--muted)}
.quote-band{left:0;top:4730px;width:1200px;height:207px;background:linear-gradient(180deg,#2a2f28,#1c1f1b 60%,#30362e)}
.quote-band p{position:absolute;left:230px;top:73px;width:740px;text-align:center;color:var(--white);font-size:15px;line-height:19px}
.footer{left:0;top:4937px;width:1200px;height:350px;background:var(--footer)}
.footnav{position:absolute;top:58px;left:0;width:1200px;display:flex;justify-content:center}
.footnav a{color:#333;text-decoration:none;font-size:13px;margin:0 33px}
.footer .btn-dark{position:absolute;left:534px;top:154px;width:133px;height:33px;background:var(--black);color:var(--white);font-size:13px;font-weight:600;border-radius:3px;display:flex;align-items:center;justify-content:center}
.footer .brand{position:absolute;left:0;width:1200px;top:242px;justify-content:center;font-size:13px;color:#444}
.footer .brand-square{width:9px;height:9px;background:#444}
.rights{position:absolute;top:283px;width:1200px;text-align:center;font-size:15px;color:#333}
</style>
</head>
<body>

<header class="abs topbar">
  <div class="brand"><span class="brand-square"></span>Corvale &amp; Associates</div>
  <div class="enquiries">for all appointments &amp; enquiries<span>90412285</span></div>
</header>
<nav class="abs mainnav">
  <a class="active">Home</a><a>Common Conditions</a><a>Specialist Clinics</a><a>Kids</a><a>About</a><a>Contact</a><a>Resources</a>
  <div class="btn-book">BOOK NOW</div>
</nav>

<h1 class="abs hero-title">Your Path to<br>Peace of Mind</h1>
<p class="abs hero-text">By creating a supportive and confidential environment we are able to work productively with every client to enable them to share their concerns, explore their issue and seek powerful solutions.</p>
<div class="photo" style="left:739px;top:261px;width:205px;height:310px">
  <div class="fill" role="img" aria-label="Young girl holding a grey rabbit, with a green wave accent" style="background:linear-gradient(160deg,#e9e4df,#c9c0b7 60%,#eeece9)"></div>
  <div class="bar"></div>
</div>

<h2 class="abs section-title" style="top:704px">Our Specialisations</h2>
<section class="abs band" style="top:765px;height:171px"></section>
<div class="abs spec-item" style="left:169px">Psychometric<br>Assessments</div>
<div class="abs divider" style="left:379px"></div>
<div class="abs spec-item" style="left:390px">Virtual<br>Reality Clinic</div>
<div class="abs divider" style="left:599px"></div>
<div class="abs spec-item" style="left:610px">Eating<br>Disorders</div>
<div class="abs divider" style="left:819px"></div>
<div class="abs spec-item" style="left:830px">FND and<br>Somatisation</div>
<div class="abs btn-outline" style="left:540px;top:970px">Learn More</div>

<h2 class="abs section-title" style="top:1127px">What We Treat</h2>

<section class="abs band" style="top:1190px;height:452px"></section>
<div class="photo" style="left:334px;top:1260px;width:208px;height:310px">
  <div class="fill" role="img" aria-label="Father hugging his young child outdoors in autumn, with a green wave accent" style="background:linear-gradient(150deg,#4e4a2e,#9a7c45 50%,#c9a46a)"></div>
  <div class="bar"></div>
</div>
<div class="abs treat" style="left:583px;top:1330px">
  <h3>Children's Mental Health</h3>
  <p>Providing specialized support for children dealing with emotional and behavioral challenges.</p>
</div>

<div class="abs treat narrow" style="left:314px;top:1825px">
  <h3>Eating Disorders</h3>
  <p>Addressing various types of eating disorders through comprehensive therapy.</p>
</div>
<div class="photo" style="left:653px;top:1713px;width:209px;height:310px">
  <div class="fill" role="img" aria-label="Plate with burger, fries and salad seen from above, with a green wave accent" style="background:linear-gradient(160deg,#f1ede6,#d9a760 45%,#cfd3c6)"></div>
  <div class="bar"></div>
</div>

<section class="abs band" style="top:2095px;height:456px"></section>
<div class="photo" style="left:334px;top:2167px;width:208px;height:310px">
  <div class="fill" role="img" aria-label="Black and white portrait of a child in a dark room, with a green wave accent" style="background:linear-gradient(160deg,#050505,#2a2a2a 50%,#0b0b0b)"></div>
  <div class="bar"></div>
</div>
<div class="abs treat" style="left:583px;top:2237px">
  <h3>Anxiety and Depression</h3>
  <p>Offering treatment for anxiety disorders, panic attacks, and depression, helping individuals manage symptoms effectively.</p>
</div>

<h2 class="abs section-title" style="top:2678px">Meet Our Team</h2>

<div class="abs member" style="left:104px;top:2830px"><div class="avatar" role="img" aria-label="Portrait of Hannah Wexford" style="background:linear-gradient(160deg,#c9a67d,#8d6a4b)"><div class="bar"></div></div><h4>Hannah Wexford</h4><p>B.Psych (Hons), M.Psych (Clinical)</p></div>
<div class="abs member" style="left:434px;top:2830px"><div class="avatar" role="img" aria-label="Portrait of Olivia Penrose" style="background:linear-gradient(160deg,#e8d4b8,#b78a64)"><div class="bar"></div></div><h4>Olivia Penrose</h4><p>B.Sc. (Psych)(Hons); MClinPsych</p></div>
<div class="abs member" style="left:767px;top:2830px"><div class="avatar" role="img" aria-label="Portrait of Janet Holloway" style="background:linear-gradient(160deg,#e6e2dc,#b48d6c)"><div class="bar"></div></div><h4>Janet Holloway</h4><p>BEd(Sec); M. Couns.; GradDipPsych;<br>BSocSc(Psych)(Honours); MClinPsych</p></div>

<div class="abs member" style="left:104px;top:3115px"><div class="avatar" role="img" aria-label="Portrait of Marcus Ellery" style="background:linear-gradient(160deg,#dedbd4,#9a7458)"><div class="bar"></div></div><h4>Marcus Ellery</h4><p>MClinPsych</p></div>
<div class="abs member" style="left:434px;top:3115px"><div class="avatar" role="img" aria-label="Portrait of Dr Mai Tran-Ellis" style="background:linear-gradient(160deg,#3c4a2e,#1e1e1e)"><div class="bar"></div></div><h4>Dr Mai Tran-Ellis</h4><p>B.A. Psych (Hons); M. Psych (Clinical); PhD</p></div>
<div class="abs member" style="left:767px;top:3115px"><div class="avatar" role="img" aria-label="Portrait of Anya Lindqvist" style="background:linear-gradient(160deg,#f2f2f2,#6b4a3e)"><div class="bar"></div></div><h4>Anya Lindqvist</h4><p>MBA, B.Psych.(Hons); M.Psych (Clinical)</p></div>

<div class="abs member" style="left:104px;top:3398px"><div class="avatar" role="img" aria-label="Portrait of Claire Ashdown" style="background:linear-gradient(160deg,#ffffff,#9b6b45)"><div class="bar"></div></div><h4>Claire Ashdown</h4><p>B.Sc (Psych) (Hons); M.Psych (Clinical)</p></div>
<div class="abs member" style="left:434px;top:3398px"><div class="avatar" role="img" aria-label="Portrait of Ruth Calloway" style="background:linear-gradient(160deg,#2f5a35,#1b2a1c)"><div class="bar"></div></div><h4>Ruth Calloway</h4><p>M.Psychol.(Clin); GradDipPsych;<br>PhD(CulSt); BA(Hons)</p></div>
<div class="abs member" style="left:767px;top:3398px"><div class="avatar" role="img" aria-label="Portrait of Vivian Lo" style="background:linear-gradient(160deg,#ffffff,#2a2220)"><div class="bar"></div></div><h4>Vivian Lo</h4><p>B.Sci (Hons)(Psych), M. Psych (Clinical)</p></div>

<div class="abs member" style="left:104px;top:3683px"><div class="avatar" role="img" aria-label="Portrait of Daniel Pryce" style="background:linear-gradient(160deg,#7a8a6a,#3a3a34)"><div class="bar"></div></div><h4>Daniel Pryce</h4><p>B.Psych.(Hons); M.Psychol.</p></div>
<div class="abs member" style="left:434px;top:3683px"><div class="avatar" role="img" aria-label="Portrait of Dr Leah Morland" style="background:linear-gradient(160deg,#f3f0ea,#c79a6a)"><div class="bar"></div></div><h4>Dr Leah Morland</h4><p>B.Sc.(Adv)(Hons)/B.A.; M.Psych (Clin); PhD</p></div>
<div class="abs member" style="left:767px;top:3683px"><div class="avatar" role="img" aria-label="Portrait of Grace Whitfield" style="background:linear-gradient(160deg,#ffffff,#3a2a24)"><div class="bar"></div></div><h4>Grace Whitfield</h4><p>B.Sc.(Psych.)(Hons); M.Psychol.</p></div>

<div class="abs member" style="left:104px;top:3968px"><div class="avatar" role="img" aria-label="Portrait of Dr Fiona Harcourt" style="background:linear-gradient(160deg,#b44a3a,#5a2a22)"><div class="bar"></div></div><h4>Dr Fiona Harcourt</h4><p>B Lib Stud, DClinPsych/MSc</p></div>
<div class="abs member" style="left:434px;top:3968px"><div class="avatar" role="img" aria-label="Portrait of Noor Haddad" style="background:linear-gradient(160deg,#f4f0ea,#5a4032)"><div class="bar"></div></div><h4>Noor Haddad</h4><p>B.Sc.(Psych.)(Hons); M.Psychol.</p></div>
<div class="abs member" style="left:767px;top:3968px"><div class="avatar" role="img" aria-label="Portrait of Dr Chris Corvale" style="background:linear-gradient(160deg,#dfe3da,#c69a7a)"><div class="bar"></div></div><h4>Dr Chris Corvale</h4><p>B.A.(Hons); M.Psychol.; PhD</p></div>

<div class="abs member" style="left:276px;top:4254px"><div class="avatar" role="img" aria-label="Portrait of Dr Elena Vukas" style="background:linear-gradient(160deg,#e6dfd2,#8a5a3e)"><div class="bar"></div></div><h4>Dr Elena Vukas</h4><p>B.A. (Hons)(Psych); M.Psych.(Clinical);<br>Grad Dip Fam Th; D. Psych.(Clinical)</p></div>
<div class="abs member" style="left:607px;top:4254px"><div class="avatar" role="img" aria-label="Portrait of Dr Helen Marsh" style="background:linear-gradient(160deg,#4a2a4a,#c8c0b8)"><div class="bar"></div></div><h4>Dr Helen Marsh</h4><p>BFA; BSc. (Psych)(Hons);<br>MClinPsych; PhD</p></div>

<div class="abs btn-outline" style="left:540px;top:4593px">Learn More</div>

<section class="abs quote-band" role="img" aria-label="Dimmed photo of people resting on grass">
  <p>Everyone is susceptible to emotional issues at some stage in their life. People have come to recognise the benefits of professional treatment for a better future. 1000's of people have received help from us in the last 20 years. A change in your life can begin right now. We can help. Our range of fully qualified clinical psychologists means that we can find the right person for you.</p>
</section>

<footer class="abs footer">
  <nav class="footnav"><a>Home</a><a>Common Conditions</a><a>Specialist Clinics</a><a>Kids</a><a>About</a><a>Contact</a><a>Resources</a></nav>
  <div class="btn-dark">BOOK NOW</div>
  <div class="brand"><span class="brand-square"></span>Corvale &amp; Associates</div>
  <p class="rights">All rights reserved.</p>
</footer>

</body>
</html>
```